Maine Organic farm needs a label design for various food products

We need a label design that we can use across a variety of vegetable-based food products that we produce using some of our organic vegetables that we grow on our farm located in Maine, USA.
Our products include:
1) a Traditional and Vegan Korean Kimchi
2) Barrow Glaze (a Korean Hot Sauce)
3) Pickle Parade Relish
4) Plumtastic Chutney
5) Seasonal Soups (many varieties, depending on what's available during the season)
6) Lone Pine Maple Syrup (we are retired from the U.S. Border Patrol, hence the name and spelling)
7) Kestrel Brook Kombucha (made with organic Maine wild blueberries)

For the Korean products (kimchi and barrow glaze) we would like to incorporate the Korean chili pepper (red) and chopsticks. The attached picture was taken from the internet, it has not been trademarked, but I am hesitant to use it as is as our business expands. Would like the "kimchi" to somehow incorporate the chopstick and pepper, but not look exactly like the attached image.

The final design should communicate farm fresh, organic, healthy and high quality ingredients, and Maine-made. All of our products go into glass jars 16oz and 8 oz. The hot sauce goes into 5.5oz and 8 oz bottles, the Maple Syrup goes into 8oz and 16oz bottles, and a 12oz bottle for the Kombucha. We will need the flexibility of changing some components of the label to accommodate each different food product.

The labels do not have the encircle the entirety of the jar. We understand that this is a tall order to fit so many different products. We are hoping that once we get the feel and design down, we can work with you for a fee outside of the competition to finalize other products labels on different sizes jars, bottles, etc. Its most important that we get the right feel for a label that can be used for a wide variety of food products.

Target Market(s)

Health conscious, foodies, local farm supporters

Font styles to use
Serif
Decorative
Script

Colors

Designer to choose colors to be used in the design.

Requirements
Must have
• Willow Ledge Farm Logo. Room for product name (interchangeable per product), ingredients list, space for jar size (8 oz, 12 oz, 16 oz). On Korean products -must have Korean hot chili pepper and chopsticks
Nice to have
• We'd like something fairly bold and rustic looking.
Should not have
• Nothing too modern or industrial looking. Nothing hippy-ish. Clean and professional. No cartoonish looking letters or designs.

```html
<!DOCTYPE html>
<html lang="en">
<head>
<meta charset="utf-8">
<title>Willow Ledge Farm — Kimchi Label</title>
<link rel="stylesheet" href="https://fonts.googleapis.com/css2?family=Fjalla+One&family=Roboto+Condensed:wght@300;400;500&display=swap">
<style>
  :root {
    --navy: #3e4a6a;
    --ink: #0f3556;
    --frame-grey: #6b6b6b;
    --paper: #e1ddd3;
    --paper-light: #ebe7df;
    --pattern: #d8d3c8;
    --field: #a4a8b9;
    --white: #ffffff;
    --text-grey: #6a6a6a;
    --sketch: #c9c4b8;
  }
  html, body {
    margin: 0;
    padding: 0;
    width: 1200px;
    height: 1200px;
    overflow: hidden;
    background: #ffffff;
  }
  .canvas {
    width: 1200px;
    height: 1200px;
    display: block;
  }
  .brand-name {
    font-family: "Fjalla One", sans-serif;
    font-size: 34px;
    fill: var(--ink);
    letter-spacing: 1px;
  }
  .product-name {
    font-family: "Fjalla One", sans-serif;
    font-size: 66px;
    fill: var(--ink);
    letter-spacing: 1px;
  }
  .origin {
    font-family: "Fjalla One", sans-serif;
    font-size: 30px;
    fill: var(--paper-light);
    letter-spacing: 4px;
  }
  .origin-small { font-size: 24px; }
  .ingredients-title {
    font-family: "Roboto Condensed", sans-serif;
    font-weight: 500;
    font-size: 20px;
    fill: var(--text-grey);
  }
  .ingredients-body {
    font-family: "Roboto Condensed", sans-serif;
    font-weight: 400;
    font-size: 14px;
    fill: var(--text-grey);
  }
  .size-label {
    font-family: "Roboto Condensed", sans-serif;
    font-size: 24px;
    fill: var(--white);
  }
  .size-unit { font-size: 17px; }
</style>
</head>
<body>
<svg class="canvas" viewBox="0 0 1000 1000" xmlns="http://www.w3.org/2000/svg">
  <!-- label outline -->
  <path class="label-edge" fill="var(--navy)"
        d="M268,130 Q268,96 302,98 C336,100 360,46 485,44 C610,46 634,100 668,98 Q705,96 705,130 L705,908 Q705,934 678,928 Q485,882 295,928 Q268,934 268,908 Z"/>
  <path class="label-paper" fill="var(--paper-light)"
        d="M279,134 Q279,108 305,110 C340,112 366,58 485,56 C604,58 630,112 665,110 Q694,108 694,134 L694,900 Q694,920 674,916 Q485,872 299,916 Q279,920 279,900 Z"/>
  <path class="label-frame" fill="var(--paper)" stroke="var(--frame-grey)" stroke-width="7"
        d="M289,138 Q289,120 308,121 C344,122 372,70 485,68 C598,70 626,122 662,121 Q684,120 684,138 L684,892 Q684,906 668,903 Q485,860 305,903 Q289,906 289,892 Z"/>

  <!-- brand -->
  <text class="brand-name" x="486" y="188" text-anchor="middle">WILLOW LEDGE FARM</text>

  <!-- upper rule -->
  <rect x="298" y="263" width="374" height="9" rx="4.5" fill="var(--frame-grey)"/>
  <rect x="298" y="276" width="374" height="3" fill="var(--frame-grey)"/>

  <!-- patterned centre band -->
  <rect x="296" y="282" width="378" height="330" fill="var(--pattern)"
        role="img" aria-label="Fine scalloped wave pattern background"/>

  <!-- product oval -->
  <ellipse cx="485" cy="446" rx="180" ry="95" fill="var(--white)"/>
  <path d="M352,386 Q485,342 618,386" fill="none" stroke="var(--field)" stroke-width="4" stroke-linecap="round"/>
  <text class="product-name" x="484" y="466" text-anchor="middle">KIMCHI</text>
  <path fill="var(--field)" role="img" aria-label="Rolling farm field rows"
        d="M335,481 L632,481 Q600,516 485,536 Q380,530 335,481 Z"/>

  <!-- origin ribbon and rule -->
  <rect x="298" y="618" width="374" height="14" rx="7" fill="var(--frame-grey)"/>
  <path d="M397,598 L572,598 L562,624 L572,650 L397,650 L407,624 Z" fill="var(--frame-grey)"/>
  <text class="origin" x="486" y="636" text-anchor="middle">M<tspan class="origin-small">AINE</tspan></text>

  <!-- chopsticks & pepper artwork -->
  <rect x="318" y="668" width="118" height="160" rx="6" fill="var(--sketch)" opacity="0.55"
        role="img" aria-label="Line sketch of chopsticks crossed with a Korean chili pepper"/>

  <!-- ingredients -->
  <text class="ingredients-title" x="457" y="682">Ingredients</text>
  <text class="ingredients-body">
    <tspan x="460" y="711" textLength="200" lengthAdjust="spacingAndGlyphs">Lorem ipsum dolor sit amet, consecte</tspan>
    <tspan x="460" y="736" textLength="176" lengthAdjust="spacingAndGlyphs">tuer adipiscing elit, Lorem ipsum</tspan>
    <tspan x="460" y="761" textLength="152" lengthAdjust="spacingAndGlyphs">dolor sit amet, consecte tuer</tspan>
    <tspan x="460" y="786" textLength="198" lengthAdjust="spacingAndGlyphs">adipiscing elit, Lorem ipsum dolor sit</tspan>
    <tspan x="460" y="811" textLength="174" lengthAdjust="spacingAndGlyphs">amet, consecte tuer adipiscing elit,</tspan>
  </text>

  <!-- jar size -->
  <rect x="583" y="836" width="72" height="30" rx="15" fill="var(--frame-grey)"/>
  <text class="size-label" x="619" y="860" text-anchor="middle">12 <tspan class="size-unit">oz</tspan></text>
</svg>
</body>
</html>
```